NCCS Brochure Design

Northbrook Council of Clinical Standards (NCCS) needs a whole new brochure. I've upload EPS logos and past brochures. Our tagline is to "modernize healthcare" and we think our brochure should reflect that, so that's the purpose of this project.

NCCS is a proven leader in healthcare education, training and
consulting services for health professionals. We’ve earned a reputation for excellence in healthcare quality improvement and management.

NCCS works to improve healthcare quality by educating healthcare professionals about healthcare best practices. We focus on instructing our clients on how to plan for, measure, and improve healthcare quality in all facilities and facets such as:

Patient Safety
Infection Control
Performance Improvement
Risk Management
Compliance and Accreditation
Health and Hospital Administration
Health Insurance
Healthcare Financial Management
Facility Management and Safety

DESIGN SUGGESTIONS:

Brochure Size: 8.5 X 11 full size brochure or 8.5 X 11 trifold brochure

Number of Pages: 2 to 3

Colors: Feel free to use a wide array of colors but try to stay away from colors that are too loud, ex: Pink, Purple, Neon Green.

Themes: Professional, Educational

Designs:

Korvel by Tobias Lindqvar

Palvex Leaflet by Derek Ostland

Gears for assembly by Quintoru

Figura de Sr KT by vrpq

http://www.plimsark.com/post/48210736651/10-creative-brochure-designs

Don't limit yourself to these examples. However, these are examples we liked
Updates

Project Deadline Extended
Reason: We would like to see more designs

We want more full page designs than tri-fold 

We are considering both tri-fold and full-page but would like to see more full page designs 

Project Deadline Extended

Project Deadline Extended
Reason: Our lead designer making the decisions on this project has been fired. I apologize for the inconvenience. We want extend the project one last time

Project Deadline Extended

Target Market(s)

Students, Doctors, and Educational Professionals

Industry/Entity Type

Healthcare

Logo Text

asdfasdf

Font styles to use
Serif
Sans Serif
Decorative
Script

Requirements
Should not have
• Pink, Purple, Neon Green colors

```html
<!DOCTYPE html>
<html lang="en">
<head>
<meta charset="utf-8">
<title>NCCS Brochure – Membership Spread</title>
<link href="https://fonts.googleapis.com/css2?family=Barlow:wght@400;500;600;700&family=Merriweather:ital,wght@0,700;1,400&display=swap" rel="stylesheet">
<style>
  :root {
    --backdrop: #d4d4d4;
    --navy: #0c1f6e;
    --navy-deep: #081650;
    --sky: #3aa0e8;
    --band: #2b8fd8;
    --band-light: #b9d6ee;
    --white: #ffffff;
    --text-soft: #dfe7ff;
    --photo-dark: #0e3a6a;
    --photo-mid: #1f6fa8;
  }
  * { box-sizing: border-box; margin: 0; padding: 0; }
  html, body { width: 1200px; height: 847px; overflow: hidden; }
  body {
    background: radial-gradient(ellipse at center, #e2e2e2 0%, var(--backdrop) 70%, #c6c6c6 100%);
    font-family: "Barlow", "Helvetica Neue", Arial, sans-serif;
    position: relative;
  }
  .spread {
    position: absolute;
    left: 120px; top: 94px;
    width: 960px; height: 660px;
    display: flex;
    box-shadow: 0 18px 40px rgba(0,0,0,0.28);
  }
  .page { width: 480px; height: 660px; position: relative; overflow: hidden; }

  /* Left page */
  .page--membership {
    background: linear-gradient(160deg, #10268a 0%, var(--navy) 45%, var(--navy-deep) 100%);
    color: var(--text-soft);
    padding: 36px 40px 0 40px;
  }
  .section-title {
    font-weight: 600; font-size: 15px; line-height: 1.2; letter-spacing: 0.3px;
    color: var(--sky); text-transform: uppercase;
  }
  .product-title {
    font-weight: 600; font-size: 12.5px; line-height: 1.25; color: var(--sky); margin-top: 7px;
  }
  .page--membership p, .page--membership li {
    font-size: 10px; line-height: 1.25; color: var(--text-soft);
  }
  .dues { font-weight: 600; color: var(--white) !important; margin-top: 2px; }
  .dues--spaced { margin-top: 8px; }
  .square-list { list-style: none; padding-left: 10px; }
  .square-list li { position: relative; padding-left: 12px; }
  .square-list li::before {
    content: ""; position: absolute; left: 0; top: 4px;
    width: 6px; height: 6px; background: var(--sky);
  }
  .benefits { margin-top: 14px; }
  .benefits .lead { font-size: 11px; line-height: 1.3; margin-top: 2px; }
  .benefit-title {
    font-weight: 600; font-size: 9.5px; line-height: 1.2; color: var(--sky); margin-top: 8px;
  }
  .page--membership .benefits p.note,
  .page--membership .benefit-list li { font-size: 9.5px; line-height: 1.2; }
  .benefit-list { list-style: disc; padding-left: 14px; }
  .page-footer {
    position: absolute; left: 0; bottom: 0; width: 100%; height: 44px;
    background: var(--band);
    border-top: 6px solid var(--band-light);
    display: flex; align-items: center; padding-left: 22px;
    color: var(--white); font-size: 11px; font-weight: 600;
  }
  .page-number { padding-right: 6px; margin-right: 6px; border-right: 1px solid var(--white); }

  /* Right page */
  .page--feature {
    background:
      radial-gradient(circle at 38% 32%, rgba(120,240,240,0.85) 0%, rgba(63,214,216,0.45) 9%, rgba(31,111,168,0) 22%),
      linear-gradient(90deg, transparent 58%, rgba(63,214,216,0.35) 62%, rgba(63,214,216,0.25) 100%),
      linear-gradient(160deg, #16304f 0%, var(--photo-dark) 25%, var(--photo-mid) 60%, #2e7fb2 100%);
  }
  .feature-quote {
    position: absolute; left: 150px; top: 420px;
    color: var(--white); text-align: center;
    text-shadow: 0 1px 3px rgba(0,0,0,0.35);
  }
  .feature-quote blockquote {
    font-family: "Merriweather", Georgia, serif; font-style: italic;
    font-size: 19px; line-height: 1.2;
  }
  .feature-quote .mark { font-style: normal; font-weight: 700; font-size: 24px; }
  .feature-quote cite {
    display: block; font-family: "Merriweather", Georgia, serif;
    font-style: normal; font-weight: 700; font-size: 15px; margin-top: 2px;
  }
</style>
</head>
<body>
  <main class="spread">
    <section class="page page--membership">
      <h2 class="section-title">Membership Products</h2>
      <p>NCCS offers several kinds of membership to meet your varied needs.</p>

      <h3 class="product-title">Personal Membership</h3>
      <p>If you want to become an NCCS member for your own personal and professional development, consider a personal membership.</p>
      <p class="dues">Annual Dues: $100</p>

      <h3 class="product-title">Group Membership</h3>
      <p>If you would like to procure membership for multiple people in your institution, consider a group membership, which offers:</p>
      <ul class="square-list">
        <li>membership for up to 15 people</li>
        <li>up to 3 subscriptions to the JNCCS, Journal of the Northbrook Council of Clinical Standards</li>
      </ul>
      <p class="dues dues--spaced">Annual Dues: $500</p>

      <h3 class="product-title">Student Membership</h3>
      <p>If you are a student studying a health related field or have an interest in improving the quality of care available to the public, consider a student membership, which gives:</p>
      <ul class="square-list">
        <li>all the benefits of regular membership</li>
        <li>special student rates to the NCCS conference</li>
      </ul>
      <p class="dues dues--spaced">Annual Dues: $25</p>

      <div class="benefits">
        <h2 class="section-title">Member Benefits</h2>
        <p class="lead">A membership with NCCS offers the benefits of an organization filled with like-minded peers. NCCS members receive also member discounts on NCCS products and services and access to member exclusive resources and opportunities.</p>

        <h4 class="benefit-title">Member Savings</h4>
        <p class="note">NCCS members receive special rates on NCCS products and services including:</p>
        <ul class="benefit-list">
          <li>All NCCS courses and educational products</li>
          <li>NCCS workshops, seminars, and conference fees</li>
          <li>Certification exams and certification renewal</li>
        </ul>

        <h4 class="benefit-title">NCCS Publications</h4>
        <ul class="benefit-list">
          <li>quarterly issues of the NCCS newsletter</li>
          <li>Biannual issues of the Journal of the Northbrook Council of Clinical Standards</li>
        </ul>

        <h4 class="benefit-title">Opportunity</h4>
        <ul class="benefit-list">
          <li>Network and receive continuous education at the NCCS annual conference</li>
          <li>Demonstrate your commitment to quality through a fellowship or certificate</li>
          <li>Access to career opportunities through our NCCS careers page</li>
        </ul>
      </div>

      <footer class="page-footer">
        <span class="page-number">8</span>
        <span>Northbrook Council of Clinical Standards</span>
      </footer>
    </section>

    <section class="page page--feature" role="img" aria-label="Photograph of a clinician in blue scrubs holding a glowing globe above an open hand beside a translucent medical interface panel">
      <div class="feature-quote">
        <blockquote><span class="mark">“</span>Don’t find fault,<br>find a remedy.<span class="mark">”</span></blockquote>
        <cite>Harlan Whitcombe</cite>
      </div>
    </section>
  </main>
</body>
</html>
```